This is book 2 to Quarry Tempest. I'm looking for something that feels similar, with the same cymatic image used on Antarctica on the first book cover (see the cover image attached; the original designer said this was the image used: https://www.filebarrow.net/s/k7vq2m9xp4tl/cymatic-image.png). Differences: the cover should be all black (no Antarctica, no globe, nothing but the image), the cymatic image kind of a pale grayish white (subtle, not calling too much attention to itself. Think the subtle dragon on "The Boy Beneath the Copper Moon"--like that sort of). Same font as before, but red this time (with the color progression like in the first one, only red instead of blue), with the title (Quarry Tempest), author name (J.L. Pome), and subtitle (Fall of the Veshtari, Book 2)

Target Market(s)

adult action/adventure and thriller readers

Industry/Entity Type

media and literature

Colors
EB3D1F
EC4F4E
F09395
F8D3D4
FCEDEE

Requirements
Must have
• look like part of the series before
Should not have
• not too busy

```html
<!DOCTYPE html>
<html lang="en">
<head>
<meta charset="utf-8">
<title>Quarry Tempest — Cover Options</title>
<link rel="stylesheet" href="https://fonts.googleapis.com/css2?family=Antonio:wght@500&family=Cinzel:wght@500;600&family=Open+Sans:wght@400&display=swap">
<style>
  :root {
    --sheet: #ffffff;
    --charcoal: #1e1f21;
    --ink: #030303;
    --pattern-soft: #3a3b3d;
    --pattern-faint: #2a2a2b;
    --red-deep: #c0392f;
    --red-main: #eb3d1f;
    --red-light: #ec4f4e;
    --white: #ffffff;
    --label: #d4d4d4;
  }
  * { margin: 0; padding: 0; box-sizing: border-box; }
  html, body { width: 1200px; height: 1200px; overflow: hidden; background: var(--sheet); }
  .sheet { position: relative; width: 1200px; height: 1200px; background: var(--sheet); }

  .cover {
    position: absolute;
    width: 370px;
    height: 555px;
    overflow: hidden;
    text-align: center;
  }
  .cover--charcoal { background: var(--charcoal); }
  .cover--black { background: var(--ink); }

  .cover__pattern {
    position: absolute;
    inset: 0;
    background:
      radial-gradient(ellipse 60% 45% at 50% 50%, transparent 0 30%, var(--pattern-faint) 55%, transparent 80%),
      radial-gradient(ellipse 70% 55% at 50% 50%, transparent 40%, var(--pattern-soft) 75%, transparent 100%);
    opacity: 0.55;
  }
  .cover--charcoal .cover__pattern { opacity: 0.35; }
  .cover__pattern--sparse {
    background: radial-gradient(ellipse 48% 42% at 50% 52%, var(--pattern-faint) 0, var(--pattern-soft) 45%, transparent 75%);
    opacity: 0.45;
  }

  .cover__title {
    position: absolute;
    left: 0; right: 0;
    top: 158px;
    font-family: "Antonio", "Oswald", sans-serif;
    font-weight: 500;
    font-size: 108px;
    line-height: 93px;
    letter-spacing: 2px;
    text-transform: uppercase;
  }
  .cover__title-line {
    display: block;
    padding: 24px 0;
    margin: -24px 0;
    background: linear-gradient(180deg, var(--red-main) 0%, var(--red-main) 22%, var(--red-light) 55%, var(--red-deep) 80%, var(--red-deep) 100%);
    -webkit-background-clip: text;
    background-clip: text;
    color: transparent;
  }
  .cover__title-line + .cover__title-line { margin-top: -24px; }
  .cover__series {
    position: absolute;
    left: 0; right: 0;
    top: 372px;
    font-family: "Cinzel", "Trajan Pro", serif;
    font-weight: 600;
    font-size: 15px;
    letter-spacing: 0.3px;
    color: var(--white);
    text-transform: uppercase;
  }
  .cover__author {
    position: absolute;
    left: 0; right: 0;
    top: 476px;
    font-family: "Cinzel", "Trajan Pro", serif;
    font-weight: 600;
    font-size: 33px;
    letter-spacing: 3px;
    color: var(--white);
    text-transform: uppercase;
  }

  .option-label {
    position: absolute;
    width: 370px;
    text-align: center;
    font-family: "Open Sans", Arial, sans-serif;
    font-size: 12px;
    color: var(--label);
  }
</style>
</head>
<body>
<main class="sheet">

  <article class="cover cover--charcoal" style="left:23px; top:22px;">
    <div class="cover__pattern" role="img" aria-label="Faint grey cymatic wave pattern radiating from the centre"></div>
    <h1 class="cover__title"><span class="cover__title-line">Quarry</span><span class="cover__title-line">Tempest</span></h1>
    <p class="cover__series">Fall of the Veshtari, Book 2</p>
    <p class="cover__author">J.L. Pome</p>
  </article>
  <p class="option-label" style="left:18px; top:581px;">Opt-4</p>

  <article class="cover cover--charcoal" style="left:415px; top:22px;">
    <div class="cover__pattern" role="img" aria-label="Faint grey cymatic wave pattern radiating from the centre"></div>
    <h1 class="cover__title"><span class="cover__title-line">Quarry</span><span class="cover__title-line">Tempest</span></h1>
    <p class="cover__series">Fall of the Veshtari, Book 2</p>
    <p class="cover__author">J.L. Pome</p>
  </article>
  <p class="option-label" style="left:418px; top:581px;">Opt-5</p>

  <article class="cover cover--black" style="left:808px; top:22px;">
    <div class="cover__pattern" role="img" aria-label="Subtle grey cymatic wave pattern on black"></div>
    <h1 class="cover__title"><span class="cover__title-line">Quarry</span><span class="cover__title-line">Tempest</span></h1>
    <p class="cover__series">Fall of the Veshtari, Book 2</p>
    <p class="cover__author">J.L. Pome</p>
  </article>
  <p class="option-label" style="left:831px; top:581px;">Opt-5a</p>

  <article class="cover cover--black" style="left:19px; top:610px;">
    <div class="cover__pattern" role="img" aria-label="Subtle grey cymatic wave pattern on black"></div>
    <h1 class="cover__title"><span class="cover__title-line">Quarry</span><span class="cover__title-line">Tempest</span></h1>
    <p class="cover__series">Fall of the Veshtari, Book 2</p>
    <p class="cover__author">J.L. Pome</p>
  </article>
  <p class="option-label" style="left:12px; top:1176px;">Opt-6</p>

  <article class="cover cover--black" style="left:415px; top:610px;">
    <div class="cover__pattern cover__pattern--sparse" role="img" aria-label="Small faint grey cymatic wave pattern centred on black"></div>
    <h1 class="cover__title"><span class="cover__title-line">Quarry</span><span class="cover__title-line">Tempest</span></h1>
    <p class="cover__series">Fall of the Veshtari, Book 2</p>
    <p class="cover__author">J.L. Pome</p>
  </article>
  <p class="option-label" style="left:410px; top:1176px;">Opt-7</p>

  <article class="cover cover--black" style="left:812px; top:610px;">
    <div class="cover__pattern" role="img" aria-label="Subtle grey cymatic wave pattern on black"></div>
    <h1 class="cover__title"><span class="cover__title-line">Quarry</span><span class="cover__title-line">Tempest</span></h1>
    <p class="cover__series">Fall of the Veshtari, Book 2</p>
    <p class="cover__author">J.L. Pome</p>
  </article>
  <p class="option-label" style="left:828px; top:1176px;">Opt-8</p>

</main>
</body>
</html>
```